Software company WebSite Design (enterprise level SW, Mobile apps, HW prototypes)

We need design for our new webpages. We got new logo and new business cards and we need webdesign which will be match with those two.
We are dealing with corporate level software development - enterprise level portals, development of optimalization SW, route planning optimalizations. For a few months we are developing mobile applications for companies.
IMPORTANT is to express the cutting edge technological company.

Target Market(s)

IT company customers

Industry/Entity Type

Business

Number of Pages Required

2 page

Requirements
Must have
• Project needs to have landing page and product detail page. Design needs to be created including full font and example images as there would be a real webpage. Design should be clean, modern and expressing hi-tech level of the company.
• Example of well designer web pages - www.quorvelt.com, www.brandissa.com - We like the font formatting and font designs (colors, placing, etc - its professional).
• Attached image contains screenshot from old web landing page. It contains basic sections of our business (Simulation Tools, Enterprise Intranet Systems, Hi-tech web presentations, Supporting Enterprise services - Optimalization and logistics monitoring)

```html
<!DOCTYPE html>
<html lang="en">
<head>
<meta charset="utf-8">
<title>Korvex Solutions</title>
<link href="https://fonts.googleapis.com/css2?family=Raleway:wght@400;500;600;700;800&family=Open+Sans:ital,wght@0,400;0,600;0,700;1,400&display=swap" rel="stylesheet">
<style>
:root{
  --orange:#e8641b;
  --blue:#2f9fd8;
  --sky:#3fc0f5;
  --ink:#3a3a3a;
  --muted:#666;
  --light:#f0f0f0;
  --footer:#2e2e2e;
  --footer-deep:#1f1f1f;
  --white:#fff;
}
*{margin:0;padding:0;box-sizing:border-box}
html,body{width:1200px;height:3758px;overflow:hidden}
body{font-family:"Open Sans",sans-serif;color:var(--ink);background:var(--white);position:relative}
section,header,footer{position:absolute;left:0;width:1200px}
.abs{position:absolute}

/* header + hero */
.hero{top:0;height:660px;background:linear-gradient(120deg,#4a4f58 0%,#6d6a66 35%,#8a8580 60%,#5d6168 100%)}
.hero-shade{position:absolute;inset:0;background:rgba(20,22,28,.35)}
.nav{top:0;height:80px;background:rgba(10,12,16,.75);z-index:2}
.brand{position:absolute;left:60px;top:20px;display:flex;align-items:center;gap:12px;font-family:"Raleway",sans-serif;font-weight:800;font-size:34px;color:var(--white);letter-spacing:1px}
.brand-mark{width:36px;height:36px;background:var(--orange)}
.nav-links{position:absolute;left:302px;top:30px;display:flex;gap:30px;font-family:"Raleway",sans-serif;font-weight:700;font-size:14px;color:var(--white)}
.sign-in{position:absolute;left:1036px;top:20px;width:104px;height:40px;border:2px solid var(--orange);border-radius:20px;color:var(--orange);font-family:"Raleway",sans-serif;font-weight:700;font-size:15px;text-align:center;line-height:36px}
.hero-title{position:absolute;top:240px;width:100%;text-align:center;font-family:"Raleway",sans-serif;font-weight:800;font-size:76px;color:var(--white);letter-spacing:1px}
.hero-sub{position:absolute;top:322px;left:150px;width:900px;text-align:center;font-family:"Raleway",sans-serif;font-size:31px;line-height:43px;color:var(--white)}

/* section headings */
.heading{display:flex;align-items:center;gap:18px;font-family:"Raleway",sans-serif;font-weight:700;font-size:27px;letter-spacing:1.5px;color:#555;text-transform:uppercase}
.heading-mark{width:32px;height:32px;background:var(--orange);border-radius:3px;transform:rotate(45deg) scale(.8)}
.heading.center{position:absolute;left:0;width:100%;justify-content:center}
.body-text{font-size:15px;line-height:27px;color:var(--muted)}
.btn-outline{position:absolute;border:2px solid var(--blue);color:#444;font-family:"Raleway",sans-serif;font-weight:700;font-size:15px;letter-spacing:1px;text-align:center;text-transform:uppercase;background:var(--white)}

/* welcome */
.welcome{top:660px;height:418px}
.welcome-art{left:55px;top:65px;width:435px;height:265px;background:linear-gradient(135deg,#eef3f7,#d9e4ee);border-radius:8px}

/* services */
.services{top:1078px;height:600px;background:linear-gradient(160deg,#3a3f45 0%,#4e5257 45%,#383c42 100%)}
.services .heading{color:var(--white);top:50px}
.service-card{position:absolute;top:170px;width:331px;height:242px;background:rgba(35,38,42,.7);border:1px solid rgba(255,255,255,.25);text-align:center}
.service-icon{position:absolute;left:130px;top:-28px;width:70px;height:70px}
.service-card h3{margin-top:78px;font-family:"Raleway",sans-serif;font-weight:700;font-size:16px;color:var(--sky);letter-spacing:.5px}
.service-card p{margin:14px auto 0;width:240px;font-size:14px;line-height:24px;color:#ddd}
.btn-orange{display:inline-block;margin-top:16px;width:130px;height:38px;line-height:38px;background:var(--orange);color:var(--white);font-family:"Raleway",sans-serif;font-weight:700;font-size:12px}
.btn-ghost{position:absolute;left:403px;top:482px;width:391px;height:60px;line-height:56px;border:2px solid var(--blue);color:var(--white);background:rgba(0,0,0,.25);font-family:"Raleway",sans-serif;font-weight:700;font-size:15px;letter-spacing:1px;text-align:center}

/* stats */
.stats{top:1678px;height:214px;background:var(--sky)}
.stat{position:absolute;top:56px;display:flex;align-items:center;gap:26px;color:var(--white)}
.stat-icon{width:76px;height:76px;border-radius:50%;background:rgba(255,255,255,.18);border:2px solid rgba(255,255,255,.35)}
.stat-num{font-family:"Raleway",sans-serif;font-weight:800;font-size:60px;line-height:62px;text-align:center}
.stat-label{font-family:"Raleway",sans-serif;font-weight:500;font-size:24px;text-align:center}

/* customers */
.customers{top:1892px;height:455px}
.customer-name{position:absolute;width:260px;text-align:center;font-family:"Raleway",sans-serif;font-weight:700;font-size:32px;color:#2c3d5a}

/* blog */
.blog{top:2347px;height:466px;background:var(--light)}
.blog-photo{left:75px;top:118px;width:421px;height:298px;background:linear-gradient(135deg,#1f4e7a,#3b6f98 45%,#b8a48c)}
.blog-title{position:absolute;left:524px;top:112px;width:580px;font-family:"Raleway",sans-serif;font-weight:700;font-size:24px;line-height:32px;color:var(--blue)}
.blog-date{position:absolute;left:524px;top:310px;font-size:14px;font-weight:600;color:var(--orange)}

/* testimonial */
.testimonial{top:2813px;height:524px}
.quote-badge{position:absolute;left:577px;top:124px;width:48px;height:48px;border-radius:50%;background:var(--blue)}
.quote-text{position:absolute;left:110px;top:198px;width:980px;text-align:center;font-style:italic;font-size:14.5px;line-height:28px;color:var(--muted)}
.avatar{position:absolute;left:543px;top:305px;width:116px;height:116px;border-radius:50%;background:linear-gradient(160deg,#c9ccd2,#4a5363)}
.avatar-name{position:absolute;top:440px;width:100%;text-align:center;font-family:"Raleway",sans-serif;font-weight:700;font-size:15px;color:var(--orange)}

/* footer */
.footer{top:3337px;height:313px;background:var(--footer)}
.footer-col{position:absolute;top:44px}
.footer-col h4{font-family:"Raleway",sans-serif;font-weight:700;font-size:15px;color:var(--orange);letter-spacing:1px;margin-bottom:16px}
.footer-col li{list-style:none;font-size:13.5px;color:#ccc;line-height:30px}
.field{width:300px;height:42px;border:1px solid #666;margin-bottom:14px;padding-left:14px;line-height:40px;font-size:13px;color:#aaa}
.signup{margin-left:190px;width:110px;height:42px;border:2px solid var(--blue);color:var(--blue);text-align:center;line-height:38px;font-family:"Raleway",sans-serif;font-weight:700;font-size:13px}
.bottom-bar{top:3650px;height:108px;background:var(--footer-deep)}
.bottom-bar .brand{top:34px;font-size:30px}
.copyright{position:absolute;left:285px;top:46px;font-size:13px;color:#aaa}
.social{position:absolute;left:898px;top:32px;display:flex;gap:12px}
.social span{width:40px;height:40px;border-radius:50%;border:2px solid #ccc}
</style>
</head>
<body>

<header class="nav">
  <div class="brand"><span class="brand-mark"></span>KORVEX</div>
  <nav class="nav-links">
    <span>Home</span><span>Products</span><span>Customers</span><span>Pricing</span><span>About Us</span><span>Enterprise</span><span>Support</span><span>Resources</span>
  </nav>
  <div class="sign-in">Sign in</div>
</header>

<section class="hero" role="img" aria-label="Photo of a team working together at computers in a bright office">
  <div class="hero-shade"></div>
  <h1 class="hero-title">KORVEX SOLUTIONS</h1>
  <p class="hero-sub">We are a software development company providing enterprise level portals, development of optimalization SW, route planning optimalizations...</p>
</section>

<section class="welcome">
  <div class="abs welcome-art" role="img" aria-label="Illustration of a desktop computer, laptop and devices with code and cloud symbols"></div>
  <h2 class="heading abs" style="left:524px;top:52px"><span class="heading-mark"></span>Welcome to our website</h2>
  <p class="abs body-text" style="left:524px;top:112px;width:590px">Vestibulum ante ipsum primis in faucibus orci luctus et ultrices posuere cubilia scelerisque ante. Duis aliquam nibh a dui iaculis viverra id a velit. Vivamus egestas risus in magna varius commodo. Sed semper viverra egestas. Etiam pretium porttitor lectus, vel ornare neque porta volutpat. Duis aliquam nibh a dui iaculis viverra id a velit. Vivamus egestas risus in magna varius commodo.<br>Sed semper viverra egestas.</p>
  <div class="btn-outline" style="left:524px;top:307px;width:166px;height:60px;line-height:56px">Read more</div>
</section>

<section class="services" role="img" aria-label="Photo of developers working at desks with monitors">
  <h2 class="heading center"><span class="heading-mark"></span>Our services</h2>
  <div class="service-card" style="left:75px">
    <svg class="service-icon" viewBox="0 0 70 70"><rect x="13" y="13" width="44" height="44" transform="rotate(45 35 35)" fill="#222"/><circle cx="35" cy="35" r="8" fill="none" stroke="#fff" stroke-width="3"/><circle cx="35" cy="35" r="2.5" fill="#fff"/></svg>
    <h3>SIMULATION TOOLS</h3>
    <p>Vestibulum ante ipsum primis in faucibus orci luctus et ultrices posuere cubilia scelerisque ante.</p>
    <span class="btn-orange">LEARN MORE</span>
  </div>
  <div class="service-card" style="left:436px">
    <svg class="service-icon" viewBox="0 0 70 70"><rect x="13" y="13" width="44" height="44" transform="rotate(45 35 35)" fill="#222"/><rect x="26" y="28" width="18" height="12" fill="none" stroke="#fff" stroke-width="2.5"/><line x1="23" y1="43" x2="47" y2="43" stroke="#fff" stroke-width="2.5"/></svg>
    <h3>ENTERPRISE INTRANET SYSTEMS</h3>
    <p>Vestibulum ante ipsum primis in faucibus orci luctus et ultrices posuere cubilia scelerisque ante.</p>
    <span class="btn-orange">LEARN MORE</span>
  </div>
  <div class="service-card" style="left:794px">
    <svg class="service-icon" viewBox="0 0 70 70"><rect x="13" y="13" width="44" height="44" transform="rotate(45 35 35)" fill="#222"/><circle cx="35" cy="35" r="9" fill="none" stroke="#fff" stroke-width="2.5"/><line x1="26" y1="35" x2="44" y2="35" stroke="#fff" stroke-width="2"/></svg>
    <h3>HI-TECH WEB PRESENTATIONS</h3>
    <p>Vestibulum ante ipsum primis in faucibus orci luctus et ultrices posuere cubilia scelerisque ante.</p>
    <span class="btn-orange">LEARN MORE</span>
  </div>
  <div class="btn-ghost">VIEW ALL SERVICES</div>
</section>

<section class="stats">
  <div class="stat" style="left:75px"><span class="stat-icon"></span><div><div class="stat-num">1.9M+</div><div class="stat-label">developers</div></div></div>
  <div class="stat" style="left:450px"><span class="stat-icon"></span><div><div class="stat-num">130K+</div><div class="stat-label">customers</div></div></div>
  <div class="stat" style="left:812px"><span class="stat-icon"></span><div><div class="stat-num">300+</div><div class="stat-label">awards</div></div></div>
</section>

<section class="customers">
  <h2 class="heading center" style="top:50px"><span class="heading-mark"></span>Our customers</h2>
  <div class="customer-name" style="left:45px;top:140px">Meridot</div>
  <div class="customer-name" style="left:316px;top:140px">Halvaro</div>
  <div class="customer-name" style="left:589px;top:140px">Tessly</div>
  <div class="customer-name" style="left:860px;top:140px">Brandt Systems</div>
  <div class="customer-name" style="left:45px;top:236px">Skyvane</div>
  <div class="customer-name" style="left:316px;top:236px">Pinnora</div>
  <div class="customer-name" style="left:589px;top:236px">Oatfield</div>
  <div class="customer-name" style="left:860px;top:236px">Calder-Moss</div>
  <div class="btn-outline" style="left:405px;top:348px;width:390px;height:60px;line-height:56px">View all services</div>
</section>

<section class="blog">
  <h2 class="heading center" style="top:46px"><span class="heading-mark"></span>Blog posts</h2>
  <div class="abs blog-photo" role="img" aria-label="Photo of a person typing on a keyboard in front of a monitor showing code"></div>
  <h3 class="blog-title">Nam fermentum vestibulum purus id aliquet aliquam nibh a dui iaculis</h3>
  <p class="abs body-text" style="left:524px;top:190px;width:590px">Vestibulum ante ipsum primis in faucibus orci luctus et ultrices posuere cubilia scelerisque ante. Duis aliquam nibh a dui iaculis viverra id a velit. Vivamus egestas risus in magna varius commodo. Sed semper viverra egestas. Etiam pretium porttitor lectus, vel ornare neque porta volutpat.</p>
  <p class="blog-date">&#9632;&nbsp; Posted on May 20, 2016</p>
  <div class="btn-outline" style="left:524px;top:358px;width:280px;height:58px;line-height:54px">Read all blog posts</div>
</section>

<section class="testimonial">
  <h2 class="heading center" style="top:58px"><span class="heading-mark"></span>What our customer says</h2>
  <svg class="quote-badge" viewBox="0 0 48 48"><circle cx="24" cy="24" r="24" fill="#2f9fd8"/><text x="24" y="33" text-anchor="middle" font-family="Raleway, sans-serif" font-weight="800" font-size="26" fill="#fff">&#8220;</text></svg>
  <p class="quote-text">Vestibulum ante ipsum primis in faucibus orci luctus et ultrices posuere cubilia scelerisque ante. Duis aliquam nibh a dui iaculis viverra id a velit. Vivamus egestas risus in magna varius commodo. Sed semper viverra egestas. Etiam pretium porttitor lectus, vel ornare neque porta volutpat. Aenean a nibh eget turpis vehicula tempus ac sed massa...</p>
  <div class="avatar" role="img" aria-label="Portrait photo of the customer"></div>
  <p class="avatar-name">Name Heading</p>
</section>

<footer class="footer">
  <div class="footer-col" style="left:75px"><h4>PRODUCTS</h4><ul><li>Aliquam molestie</li><li>Imperdiet euismod</li><li>Dui purus auctor</li><li>Tellus et interdum</li><li>Lacus lectus</li><li>Aenean a nibh</li><li>Eget turpis</li></ul></div>
  <div class="footer-col" style="left:333px"><h4>COMPANY</h4><ul><li>About Us</li><li>Customers</li><li>Partners</li><li>Blog</li><li>Jobs</li><li>Press</li><li>Pricing</li></ul></div>
  <div class="footer-col" style="left:538px"><h4>CONNECT</h4><ul><li>Developer Support</li><li>Resources</li><li>Consulting Services</li><li>Contact Sales</li><li>Chirpline</li><li>CodeHarbor</li><li>Query Depot</li></ul></div>
  <div class="footer-col" style="left:794px"><h4>NEWSLLTER SIGN UP</h4><div class="field">Enter Name</div><div class="field">Enter Email Address</div><div class="signup">SIGN UP</div></div>
</footer>

<div class="abs bottom-bar" style="left:0;width:1200px">
  <div class="brand"><span class="brand-mark"></span>KORVEX</div>
  <p class="copyright">Copyright © 2016. All Right Reserved</p>
  <div class="social"><span></span><span></span><span></span><span></span><span></span></div>
</div>

</body>
</html>
```